Web Design Project - Event Management Company

A web-page design needs to be created for an event management company. The logo has already been created, the design needs to draw on the themes and colors of the logo and extend on that.

The event management company likes to differentiate itself from others by being a bit "un-conventional" and being able to think outside the box.

the specialise in corporate events, weddings, AGMs, anything that requires coordination of resources. They also can provide Audio Visual services such as recording events.

final design will also require HTML implementation

```html
<!DOCTYPE html>
<html lang="en">
<head>
<meta charset="utf-8">
<title>Bright Block Events</title>
<link href="https://fonts.googleapis.com/css2?family=PT+Sans:wght@400;700&family=PT+Sans+Narrow&family=Roboto+Condensed:wght@400&display=swap" rel="stylesheet">
<style>
  :root{
    --pink:#f6c3d3;
    --red:#e8532a;
    --sky:#6cc6e3;
    --lime:#d4d41c;
    --orange:#f29a2e;
    --orange-dark:#e37e14;
    --olive:#b4b512;
    --blue:#2aa0cc;
    --ink:#333;
    --text:#555;
    --muted:#8a8a8a;
    --line:#dcdcdc;
  }
  *{box-sizing:border-box;margin:0;padding:0}
  html,body{width:1112px;height:1200px;overflow:hidden;background:#fff}
  body{position:relative;font-family:"PT Sans",sans-serif;color:var(--text)}

  .top-stripe{position:absolute;left:0;top:0;width:100%;height:10px;display:flex}
  .top-stripe span{flex:1}

  .hero-bg{position:absolute;left:0;top:10px;width:100%;height:360px;
    background:linear-gradient(#fff 0,#fff 55%,#f1f1f1 100%)}
  .swoosh{position:absolute;left:0;top:300px;width:1112px;height:90px}

  .brand{position:absolute;left:116px;top:78px;display:flex;align-items:center;gap:12px}
  .brand-mark{width:38px;height:38px;background:var(--orange)}
  .brand-name{font-family:"Roboto Condensed",sans-serif;font-size:33px;color:#4a4a4a;letter-spacing:.5px;line-height:1}

  .booking{position:absolute;left:779px;top:44px;width:216px;text-align:center}
  .booking-label{font-size:17px;color:#444;line-height:1}
  .booking-phone{font-size:21px;color:var(--orange);margin-top:4px;line-height:1}
  .search{position:absolute;left:779px;top:99px;width:216px;height:28px;border:1px solid var(--line);background:#fff}
  .search span{position:absolute;left:11px;top:7px;font-size:11px;font-style:italic;color:#888}
  .search svg{position:absolute;right:10px;top:6px}

  .main-nav{position:absolute;left:116px;top:138px;width:880px;height:48px;display:flex;
    background:linear-gradient(#f9b048,#ef8d1f);border:1px solid #dd7d15;border-radius:2px}
  .main-nav a{display:flex;align-items:center;justify-content:center;color:#fff;text-decoration:none;
    font-family:"PT Sans Narrow",sans-serif;font-size:17px;border-left:1px solid #d97a12;
    box-shadow:inset 1px 0 0 #fbbd63}
  .main-nav a:first-child{border-left:0;box-shadow:none}

  .slider{position:absolute;left:114px;top:187px;width:882px;height:338px;background:#fff;
    border:1px solid #e4e4e4;box-shadow:0 1px 3px rgba(0,0,0,.08)}
  .slide-photo{position:absolute;left:6px;top:3px;width:869px;height:329px;
    background:radial-gradient(ellipse at 50% 30%,#3ab6e8 0,#1a3a7a 30%,#1b1430 55%,transparent 70%),
      linear-gradient(#10131f 0,#2a2030 45%,#c86a6e 70%,#d9a07a 100%)}
  .caption{position:absolute;left:6px;top:140px;width:336px;height:136px;background:rgba(40,40,40,.85);border-radius:0 0 4px 0;color:#fff;padding:24px 0 0 29px}
  .caption-kicker{font-size:22px;line-height:1.1}
  .caption-title{font-size:34px;line-height:1.15}
  .caption-sub{font-size:14.5px;margin-top:4px}
  .dots{position:absolute;left:419px;top:312px;display:flex;gap:5px}
  .dots span{width:9px;height:9px;border-radius:50%;background:#555;opacity:.8}
  .arrows{position:absolute;left:832px;top:302px}

  .services{position:absolute;left:126px;top:550px;width:858px;display:flex;justify-content:space-between}
  .service{width:268px}
  .service-photo{height:118px;border-radius:18px 18px 18px 0}
  .service h3{font-weight:400;font-size:20px;margin:10px 0 4px 3px}
  .service p{font-size:13px;line-height:20px;color:var(--muted);margin-left:3px;width:265px}
  .btn{display:inline-block;margin:12px 0 0 3px;width:101px;height:30px;line-height:30px;text-align:center;
    color:#fff;font-size:12px;border-radius:2px;text-decoration:none}
  .weddings h3{color:#e0401c}.weddings .btn{background:linear-gradient(#f06840,#d8411a)}
  .av h3{color:var(--olive)}.av .btn{background:linear-gradient(#d3d43a,#aeb014)}
  .corporate h3{color:var(--blue)}.corporate .btn{background:linear-gradient(#4bb9e1,#1f8fc0)}

  .welcome{position:absolute;left:120px;top:828px;width:565px}
  .welcome h1{font-weight:400;font-size:27.5px;color:var(--ink);line-height:1.1}
  .welcome .lead{font-size:15.5px;color:#444;margin-top:8px}
  .welcome p.body{font-size:11.3px;line-height:21px;color:var(--text);margin-top:8px}
  .welcome p.body + p.body{margin-top:8px}

  .video{position:absolute;left:716px;top:815px;width:284px;height:236px;border-radius:3px 3px 0 0;
    background:linear-gradient(#7fd0ea,#3fb0d9);border-bottom-left-radius:40px 10px;border-bottom-right-radius:40px 10px}
  .video h2{font-weight:400;color:#fff;font-size:20.5px;margin:16px 0 0 21px}
  .video-frame{position:absolute;left:18px;top:48px;width:248px;height:165px;border:2px solid #fff;
    background:linear-gradient(#f2eef2,#e8d3e6 45%,#a4407f 100%)}
  .play{position:absolute;left:105px;top:60px}

  .footer{position:absolute;left:0;top:1097px;width:100%;height:103px;background:linear-gradient(#ececec,#fff 30%)}
  .footer-nav{position:absolute;left:117px;top:28px;font-size:13px;color:#444}
  .footer-nav a{color:#444;text-decoration:none}
  .footer-nav i{font-style:normal;margin:0 5px}
  .copyright{position:absolute;left:119px;top:57px;font-size:9.5px;color:var(--muted)}
  .social{position:absolute;left:916px;top:35px;display:flex;gap:5px}
  .social span{width:20px;height:19px;border-radius:2px}
</style>
</head>
<body>
  <div class="top-stripe">
    <span style="background:var(--pink)"></span><span style="background:var(--red)"></span><span style="background:var(--sky)"></span><span style="background:var(--lime)"></span><span style="background:var(--orange)"></span>
  </div>
  <div class="hero-bg"></div>
  <svg class="swoosh" viewBox="0 0 1112 90" aria-hidden="true">
    <path d="M0 17 Q60 20 120 34 L120 44 Q60 30 0 27Z" fill="var(--orange)"/>
    <path d="M0 27 Q60 30 120 44 L120 52 Q60 38 0 36Z" fill="var(--red)"/>
    <path d="M0 36 Q60 38 120 52 L120 60 Q60 46 0 45Z" fill="var(--sky)"/>
    <path d="M0 45 Q60 46 120 60 L120 68 Q60 56 0 55Z" fill="var(--pink)"/>
    <path d="M992 36 Q1050 24 1112 18 L1112 27 Q1050 33 992 45Z" fill="var(--orange)"/>
    <path d="M992 45 Q1050 33 1112 27 L1112 35 Q1050 41 992 53Z" fill="var(--red)"/>
    <path d="M992 53 Q1050 41 1112 35 L1112 43 Q1050 49 992 61Z" fill="var(--sky)"/>
    <path d="M992 61 Q1050 49 1112 43 L1112 52 Q1050 58 992 70Z" fill="var(--pink)"/>
  </svg>

  <header>
    <div class="brand"><span class="brand-mark"></span><span class="brand-name">BRIGHT BLOCK EVENTS</span></div>
    <div class="booking">
      <div class="booking-label">Booking Now</div>
      <div class="booking-phone">555.014.2288</div>
    </div>
    <div class="search"><span>Search here..</span>
      <svg width="15" height="15" viewBox="0 0 15 15"><circle cx="6" cy="6" r="4.5" fill="none" stroke="#999" stroke-width="2"/><path d="M9.5 9.5L13.5 13.5" stroke="#999" stroke-width="2.5" stroke-linecap="round"/></svg>
    </div>
    <nav class="main-nav">
      <a style="width:101px">HOME</a><a style="width:113px">ABOUT US</a><a style="width:105px">SERVICES</a><a style="width:116px">PROGRAMS</a><a style="width:97px">GALLERY</a><a style="width:90px">HIRE US</a><a style="width:139px">TESTIMOIALS</a><a style="width:119px">CONTACT</a>
    </nav>
  </header>

  <section class="slider">
    <div class="slide-photo" role="img" aria-label="Banquet hall set for a gala dinner with stage lighting and screens"></div>
    <div class="caption">
      <div class="caption-kicker">Specialise in Organise</div>
      <div class="caption-title">Events &amp; Weddings</div>
      <div class="caption-sub">Duis sed tellus et tortor vestibulum</div>
    </div>
    <div class="dots"><span></span><span></span><span></span><span></span></div>
    <svg class="arrows" width="24" height="20" viewBox="0 0 24 20" aria-hidden="true"><path d="M9 3L3 10L9 17M15 3L21 10L15 17" fill="none" stroke="#fff" stroke-width="2.5"/></svg>
  </section>

  <section class="services">
    <article class="service weddings">
      <div class="service-photo" role="img" aria-label="Wine glasses and folded napkins on a reception table" style="background:linear-gradient(135deg,#a5492a,#e7a36b 50%,#f4ddc4)"></div>
      <h3>Weddings &amp; Special Programs</h3>
      <p>Phasellus felis dolor, scelerisque a, tempus eget, lobortis id, libero. Donec scelerisque</p>
      <a class="btn">READ MORE</a>
    </article>
    <article class="service av">
      <div class="service-photo" role="img" aria-label="Conference table with microphones" style="background:linear-gradient(#6b6a70,#9d9aa0 55%,#e9e7e6)"></div>
      <h3>Audio Visual Services</h3>
      <p>Phasellus felis dolor, scelerisque a, tempus eget, lobortis id, libero. Donec scelerisque</p>
      <a class="btn">READ MORE</a>
    </article>
    <article class="service corporate">
      <div class="service-photo" role="img" aria-label="Guests at a corporate evening event" style="background:linear-gradient(120deg,#2a2830,#6a5a55 50%,#c9b3a6)"></div>
      <h3>Corporate Events</h3>
      <p>Phasellus felis dolor, scelerisque a, tempus eget, lobortis id, libero. Donec scelerisque</p>
      <a class="btn">READ MORE</a>
    </article>
  </section>

  <section class="welcome">
    <h1>Welcome to Bright Block Events</h1>
    <p class="lead">Lorem ipsum dolor sit amet, consectetuer adipiscing elit. Nam cursus. Morbi ut mi</p>
    <p class="body">Nunc tempus felis vitae urna. Vivamus porttitor, g, purus nisi eleifend libero, a tempus libero lectus feugiat felis. Morbi diam mauris, viverra in, gravida eu, mattis in, ante. Morbi eget arcu. Morbi porta, libero id ullamcorper nonummy, nibh ligula pulvinar metus, eget consectetuer augue nisi quis lacus.</p>
    <p class="body">Ut ac mi quis lacus mollis aliquam. Curabitur iaculis tempus eros. Curabitur vel mi sit amet magna malesuada ultrices. Ut nisi erat, fermentum vel, congue id, euismod in, elit. Fusce ultricies, orci ac feugiat suscipit, leo massa sodales velit, et scelerisque mi tortor at ipsum.</p>
  </section>

  <aside class="video">
    <h2>Watch Our Video</h2>
    <div class="video-frame" role="img" aria-label="Wedding reception tables with white chair covers and purple sashes">
      <svg class="play" width="40" height="40" viewBox="0 0 40 40" aria-hidden="true"><circle cx="20" cy="20" r="19" fill="#111" stroke="#fff" stroke-width="2"/><path d="M16 12L28 20L16 28Z" fill="#fff"/></svg>
    </div>
  </aside>

  <footer class="footer">
    <nav class="footer-nav"><a>Home</a><i>|</i><a>About Us</a><i>|</i><a>Services</a><i>|</i><a>Programs</a><i>|</i><a>Gallery</a><i>|</i><a>Hire us</a><i>|</i><a>Testimoinals</a><i>|</i><a>Contact</a></nav>
    <div class="copyright">Copyright © 2013 Company Name.&nbsp; All right reserved.&nbsp; Term of Use</div>
    <div class="social" aria-label="Social links"><span style="background:#5bbde6"></span><span style="background:#2f7fb8"></span><span style="background:#4a6db0"></span></div>
  </footer>
</body>
</html>
```